Pharma compliance business needs an eye catching academic poster

Academic poster for display at a pharma industry conference

Background

ClinoVerse Ltd is an online, on-demand supplier of compliance advice (copy review) to the life science industry. See www.clinoverse-demo.co.uk for more info.

We have conducted a benchmarking study on the time spent by three large pharma companies on copy review. It highlights time spent and time wasted as a result of unnecessary, additional rounds of review. As a result we have developed recommendation for improving the copy review process.

Requirement

We need an academic poster A0 Landscape (841 x 1189 mm) that summaries our methodology, results and conclusions. We have written the copy - see attached.

This poster will be displayed at the QTE 8th Annual Continental Health Knowledge and Outreach Summit - See more at: http://www.qtehub-example.org/Events-and-Courses/Find-Events-and-Courses/Event-Details.aspx?ProductID=7481536&EventType=Meeting#sthash.kW4pQx2n.dpuf.

Audience

Attendees of this conference are budget holders and decision makers. They can chose to outsource copy review to organisation like ours, however, many pharma companies currently keep this function is house and waste internal resource, time and money.

Objective

Our objective is demonstrate from our findings that massive savings can be found by getting copy right first time.

Design Guidelines

This poster should not be heavily branded - as this CANNOT be promotional however you may include our logo with the authors names. We would like you to use our brand guidelines, however, in order that it is clear that this study was conducted by ourselves. Brand book is attached plus our logos and icons.

Examples of academic posters can be found with a quick google search - one source that I have found useful is http://brendalowicke-example.com/tips/academic/posterdesign I have attached an example of the kind of layout we would like to see... please keep the background quite plain as this will make it easier to read

Within the copy attached data graphs have been included for position guidance only and an excel file with the raw data and graphs is also attached - if you feel that the data can be displayed more effectively please do... also please apply our brand style. It is important that the data is accurately reproduced.

```html
<!DOCTYPE html>
<html lang="en">
<head>
<meta charset="utf-8">
<title>Copy Review Resource Utilisation – Poster</title>
<link rel="stylesheet" href="https://fonts.googleapis.com/css2?family=Arimo:wght@400;700&display=swap">
<style>
:root{
  --page:#e4e5e8;
  --panel:#ffffff;
  --results-bg:#d8dadd;
  --header-top:#8d9db5;
  --header-bottom:#c9d0db;
  --ink:#2b2b2b;
  --muted:#555a60;
  --box:#e6e7e9;
  --teal:#4f9a96;
  --teal-dark:#2f7a78;
  --blue:#4c9cc4;
  --blue-dark:#2c6f96;
  --purple:#6f5e8c;
  --purple-dark:#54456f;
  --navy:#2a4766;
  --navy-dark:#1c3450;
  --chart-purple:#6e5a88;
  --chart-teal:#3f9a8c;
  --chart-sky:#5aaed0;
  --chart-navy:#2d4e6c;
  --axis:#9a9a9a;
}
*{box-sizing:border-box;margin:0;padding:0}
html,body{width:1200px;height:848px;overflow:hidden}
body{background:var(--page);font-family:"Arimo",Arial,sans-serif;color:var(--ink);position:relative}
.poster-header{position:absolute;left:0;top:0;width:1200px;height:140px;
  background:linear-gradient(180deg,var(--header-top),var(--header-bottom));
  border-bottom:3px solid #fff;text-align:center;color:#fff}
.poster-title{margin-top:30px;font-weight:700;font-size:23px;line-height:31px;letter-spacing:1.2px;text-transform:uppercase}
.poster-authors{margin-top:8px;font-size:10.5px;line-height:14px}
.panel{position:absolute;background:var(--panel);border-radius:12px;box-shadow:0 1px 3px rgba(0,0,0,.12)}
.pill{margin:8px 6px 0;height:28px;border-radius:14px;color:#fff;font-weight:700;font-size:15px;
  line-height:28px;text-align:center;letter-spacing:.5px}
.pill-teal{background:linear-gradient(180deg,#7cbcb8,var(--teal-dark))}
.pill-purple{background:linear-gradient(180deg,#9282ac,var(--purple-dark))}
.pill-blue{background:linear-gradient(180deg,#7cbcdc,var(--blue-dark))}
.pill-navy{background:linear-gradient(180deg,#4c6a8a,var(--navy-dark))}
p,li{font-size:7.2px;line-height:9.2px}
.intro{left:20px;top:152px;width:250px;height:450px;padding:0 0 0}
.intro .body{padding:14px 12px 0}
.intro p{margin-bottom:8px}
.grey-box{background:var(--box);padding:10px;}
.code-box{display:flex;gap:8px;margin:6px 0 12px;padding:10px 8px}
.code-box>div{flex:1}
.code-box div+div{border-left:1px solid #c9cacc;padding-left:8px}
ul{list-style:none}
ul li{padding-left:7px;position:relative;margin-bottom:6px}
ul li::before{content:"•";position:absolute;left:0}
.aims{margin:10px 0 8px;padding:12px 12px 6px}
.aims p{text-align:center;margin-bottom:8px}
.centered{text-align:center}
.method{left:20px;top:612px;width:250px;height:200px}
.method .grey-box{margin:14px 12px 12px;padding:10px 10px 4px}
.results{left:285px;top:152px;width:876px;height:660px;background:var(--results-bg)}
.card{position:absolute;background:#fff;border-radius:8px;padding:8px 10px}
.card h4{font-size:8px;text-align:center;margin:4px 0 2px}
.legend{font-size:4.6px;fill:#444}
svg text{font-family:"Arimo",Arial,sans-serif}
.card-usage{left:15px;top:53px;width:412px;height:138px}
.card-usage p{padding:4px 6px 0}
.charts-row{display:flex;justify-content:space-between;margin-top:4px}
.card-reasons{left:427px;top:53px;width:449px;height:145px;border-radius:0 8px 8px 0;display:flex}
.reasons-lead{width:90px;padding:4px 2px}
.reasons-lead p{margin-bottom:6px}
.reasons-table{flex:1;border-collapse:collapse;font-size:6.6px;margin:-2px 0 0}
.reasons-table th,.reasons-table td{border-bottom:1px solid #d6d6d8;height:15.5px;padding:0 6px;text-align:left;font-weight:400}
.reasons-table .span-head{text-align:center;border:1px solid #d6d6d8}
.reasons-table td.num{width:40px;text-align:center;padding-left:0}
.card-themes{left:427px;top:205px;width:449px;height:112px;display:flex;gap:18px;padding:12px}
.abbrev{width:95px;font-size:7px;line-height:9px;padding-top:16px}
.abbrev span{display:block;margin-bottom:6px}
.card-pie{left:15px;top:195px;width:196px;height:162px}
.card-rounds{left:220px;top:195px;width:207px;height:162px}
.card-hours{left:15px;top:365px;width:412px;height:125px}
.hours-row{display:flex;justify-content:space-between}
.hours-row>div{width:128px}
.card-friction{left:15px;top:497px;width:196px;height:152px}
.card-deadlines{left:220px;top:497px;width:207px;height:152px}
.card-friction h3,.card-deadlines h3{font-size:8.4px;text-align:center;margin:2px 0 6px}
.conclusions{left:730px;top:470px;width:431px;height:342px}
.conclusions .body{padding:12px 14px 0}
.conclusions p{margin-bottom:7px;font-size:6.8px;line-height:8.6px}
.conclusions .grey-box{margin:8px 10px 0;padding:10px 14px 4px}
.conclusions .grey-box p{text-align:center}
.signoff{position:absolute;left:845px;top:768px;display:flex;align-items:center;gap:8px}
.brand-mark{display:flex;align-items:center;gap:5px;font-size:12px;font-weight:700;color:var(--navy)}
.brand-mark i{display:block;width:14px;height:14px;border-radius:50%;background:var(--navy)}
.email{font-size:12px;color:var(--navy);margin-left:20px}
</style>
</head>
<body>
<header class="poster-header">
  <h1 class="poster-title">A survey of three pharmaceutical companies’ resource utilisation in<br>copy review activities and proposals for business process improvement</h1>
  <div class="poster-authors">Mara Quill, Director, ClinoVerse Ltd, London<br>Owen Tate, Director, ClinoVerse Ltd, London</div>
</header>

<section class="panel intro">
  <div class="pill pill-teal">INTRODUCTION</div>
  <div class="body">
    <p>Promotional and non-promotional materials are highly visible outputs of pharmaceutical companies. They are scrutinised by competitors, agencies and sometimes customers. Penalties for errors can be significant, measured in time, reputation or monetary fines.</p>
    <div class="grey-box code-box">
      <div>
        <p>Central to nearly all codes and systems are requirements that statements and messages are:</p>
        <ul>
          <li>Consistent with the marketing authorisation;</li>
          <li>Accurate and capable of substantiation;</li>
          <li>Fair, balanced and up to date.</li>
        </ul>
      </div>
      <div>
        <p>Regional and national differences exist in the regulation of:</p>
        <ul>
          <li>Meetings;</li>
          <li>Gifts, fees, hospitality and travel;</li>
          <li>External approval requirements;</li>
          <li>Dispute resolution.</li>
        </ul>
      </div>
    </div>
    <p>The UK industry body, BAPM, issued a code of conduct in 1958. Its current form is very similar to the European industry EAPM code. Many UK pharmaceutical companies place considerable importance on adherence to the code, with large teams working on the review of materials and activities.</p>
    <p>Copy review is a now a significant activity that consumes considerable resources, in the form of time, of some of the most expensive and scientifically able members of staff.</p>
    <div class="grey-box aims">
      <p>The aims of this study were to,</p>
      <ul>
        <li>Quantify time taken up by copy review activities in a sample of UK pharmaceutical affiliates medical affairs and commercial functions;</li>
        <li>Identify the origins and consequences of avoidable re-work;</li>
        <li>Develop solutions.</li>
      </ul>
    </div>
    <p class="centered">We present here the medical affairs results.</p>
  </div>
</section>

<section class="panel method">
  <div class="pill pill-purple">METHOD</div>
  <div class="grey-box">
    <p style="margin-bottom:7px">We developed an online survey with three components:</p>
    <ul>
      <li>Retrospective, quantitative estimates of time taken on copy review and numbers of avoidable iterations;</li>
      <li>Ranking the common reasons for avoidable iterations;</li>
      <li>Free text responses describing potential solutions.</li>
    </ul>
  </div>
  <p class="centered" style="padding:0 24px">This was sent to 249 staff in three UK pharmaceutical companies in 2013 and 2014.</p>
</section>

<section class="panel results">
  <div class="pill pill-blue" style="height:30px;line-height:30px">RESULTS</div>

  <div class="card card-usage">
    <p>We received 118 usable responses from 249 invitations, a response rate of 47%. 48 responses were from medical affairs and 70 from commercial and other functions. The proportion of the working week spent on copy review by physicians was a consistent 40%. For medical information, the proportion varied between zero and 65%. Scientific advisors spent 0% to 42% of their time on copy activities.</p>
    <div class="charts-row">
      <svg width="128" height="76" viewBox="0 0 128 76" aria-label="Company A: percent of working week on copy">
        <g font-size="4.5" fill="#555" text-anchor="end">
          <text x="20" y="57">0</text><text x="20" y="47">10</text><text x="20" y="37">20</text><text x="20" y="27">30</text><text x="20" y="17">40</text><text x="20" y="7">50</text>
        </g>
        <text x="8" y="34" font-size="5" fill="#555">%</text>
        <line x1="22" y1="55" x2="122" y2="55" stroke="var(--axis)" stroke-width=".5"/>
        <rect x="32" y="17" width="12" height="38" fill="var(--chart-purple)"/>
        <rect x="98" y="13" width="12" height="42" fill="var(--chart-purple)"/>
        <g font-size="4.5" fill="#555" text-anchor="middle"><text x="38" y="61">Med affs</text><text x="71" y="61">Med info</text><text x="104" y="61">SA/MSL</text></g>
        <rect x="24" y="67" width="4" height="4" fill="var(--chart-purple)"/>
        <text class="legend" x="30" y="71">% of working week on copy Company A</text>
      </svg>
      <svg width="128" height="76" viewBox="0 0 128 76" aria-label="Company B: percent of working week on copy">
        <g font-size="4.5" fill="#555" text-anchor="end">
          <text x="20" y="57">0</text><text x="20" y="40">20</text><text x="20" y="24">40</text><text x="20" y="7">60</text>
        </g>
        <text x="8" y="34" font-size="5" fill="#555">%</text>
        <line x1="22" y1="55" x2="122" y2="55" stroke="var(--axis)" stroke-width=".5"/>
        <rect x="32" y="19" width="12" height="36" fill="var(--chart-teal)"/>
        <rect x="65" y="17" width="12" height="38" fill="var(--chart-teal)"/>
        <rect x="98" y="32" width="12" height="23" fill="var(--chart-teal)"/>
        <g font-size="4.5" fill="#555" text-anchor="middle"><text x="38" y="61">Med affs</text><text x="71" y="61">Med info</text><text x="104" y="61">SA/MSL</text></g>
        <rect x="24" y="67" width="4" height="4" fill="var(--chart-teal)"/>
        <text class="legend" x="30" y="71">% of working week on copy Company B</text>
      </svg>
      <svg width="128" height="76" viewBox="0 0 128 76" aria-label="Company C: percent of working week on copy">
        <g font-size="4.5" fill="#555" text-anchor="end">
          <text x="20" y="57">0</text><text x="20" y="45">20</text><text x="20" y="32">40</text><text x="20" y="20">60</text><text x="20" y="7">80</text>
        </g>
        <text x="8" y="34" font-size="5" fill="#555">%</text>
        <line x1="22" y1="55" x2="122" y2="55" stroke="var(--axis)" stroke-width=".5"/>
        <rect x="32" y="30" width="12" height="25" fill="var(--chart-sky)"/>
        <rect x="65" y="14" width="12" height="41" fill="var(--chart-sky)"/>
        <g font-size="4.5" fill="#555" text-anchor="middle"><text x="38" y="61">Med affs</text><text x="71" y="61">Med info</text><text x="104" y="61">SA/MSL</text></g>
        <rect x="24" y="67" width="4" height="4" fill="var(--chart-sky)"/>
        <text class="legend" x="30" y="71">% of working week on copy Company C</text>
      </svg>
    </div>
  </div>

  <div class="card card-reasons">
    <div class="reasons-lead">
      <p>The three top-ranked reasons for re-work were:</p>
      <ul>
        <li>Claims not supported;</li>
        <li>References missing or not marked up;</li>
        <li>Differences of opinion.</li>
      </ul>
    </div>
    <table class="reasons-table">
      <tr><th></th><th></th><th></th><th class="span-head">Ranked reasons for re-work</th></tr>
      <tr><th>A</th><th>B</th><th>C</th><th></th></tr>
      <tr><td class="num">1</td><td class="num">1</td><td class="num">2</td><td>Claims not supportable</td></tr>
      <tr><td class="num">2</td><td class="num">2</td><td class="num">1</td><td>References missing or not marked</td></tr>
      <tr><td class="num">3</td><td class="num">4</td><td class="num">4</td><td>Difference in opinion in interpreting the Code</td></tr>
      <tr><td class="num">6</td><td class="num">3</td><td class="num">3</td><td>Spelling and grammar</td></tr>
      <tr><td class="num">4</td><td class="num">5</td><td class="num">6</td><td>Other technical Code issue</td></tr>
      <tr><td class="num">5</td><td class="num">7</td><td class="num">5</td><td>Review criteria changed during project</td></tr>
      <tr><td class="num">7</td><td class="num">6</td><td class="num">7</td><td>Layout or presentation</td></tr>
    </table>
  </div>

  <div class="card card-themes">
    <div class="abbrev"><span>SA<br>Scientific Affairs</span><span>MSL<br>Medical Science Liaison</span></div>
    <div>
      <p style="margin-bottom:5px">Free text proposed solutions from respondents were grouped subjectively into themes. The three most frequent cited proposals were:</p>
      <ul>
        <li>Meetings to discuss materials before copy got into the review cycle;</li>
        <li>Improve the scientific accuracy and spelling of copy before review, so that it is right first time;</li>
        <li>Insist on consistency between reviewers and between review cycles.</li>
      </ul>
    </div>
  </div>

  <div class="card card-pie">
    <p>On average just over 50% of time spent on copy activities went on checking scientific statements and claims. The remainder was spent on concept and planning meetings, commissioning, proof reading, compiling materials. Rounds of scheduled review averaged 2.3.</p>
    <svg width="176" height="96" viewBox="0 0 176 96" aria-label="Pie chart: percent of copy time by activity, all medical affairs">
      <g transform="translate(40,52)">
        <path d="M0 0 L0 -38 A38 38 0 1 1 -11.7 36.1 Z" fill="var(--chart-sky)"/>
        <path d="M0 0 L-11.7 36.1 A38 38 0 0 1 -33.6 -17.7 Z" fill="var(--chart-teal)"/>
        <path d="M0 0 L-33.6 -17.7 A38 38 0 0 1 -20.6 -31.9 Z" fill="var(--chart-navy)"/>
        <path d="M0 0 L-20.6 -31.9 A38 38 0 0 1 0 -38 Z" fill="var(--chart-purple)"/>
      </g>
      <text x="88" y="10" font-size="7.2" font-weight="700">% of copy time by activity,</text>
      <text x="96" y="19" font-size="7.2" font-weight="700">all medical affairs</text>
      <g font-size="4.8" fill="#444">
        <rect x="92" y="32" width="4" height="4" fill="var(--chart-sky)"/><text x="99" y="36">Statemetns and claims</text>
        <rect x="92" y="46" width="4" height="4" fill="var(--chart-teal)"/><text x="99" y="50">Meetings</text>
        <rect x="92" y="60" width="4" height="4" fill="var(--chart-navy)"/><text x="99" y="64">Compiling</text>
        <rect x="92" y="74" width="4" height="4" fill="var(--chart-purple)"/><text x="99" y="78">Commissioning</text>
      </g>
    </svg>
  </div>

  <div class="card card-rounds">
    <p>Estimates of the proportion of jobs requiring additional avoidable rounds of review ranged between 30 and 50%.</p>
    <svg width="187" height="118" viewBox="0 0 187 118" aria-label="Bar chart: percent jobs needing extra rounds">
      <text x="93" y="16" font-size="7.6" font-weight="700" text-anchor="middle">% jobs needing extra rounds</text>
      <g font-size="4.5" fill="#555" text-anchor="end">
        <text x="30" y="102">0</text><text x="30" y="88">10</text><text x="30" y="74">20</text><text x="30" y="60">30</text><text x="30" y="46">40</text><text x="30" y="32">50</text><text x="30" y="18">60</text>
      </g>
      <text x="16" y="62" font-size="5" fill="#555">%</text>
      <line x1="33" y1="100" x2="172" y2="100" stroke="var(--axis)" stroke-width=".5"/>
      <rect x="50" y="26" width="16" height="74" fill="var(--chart-navy)"/>
      <rect x="93" y="37" width="16" height="63" fill="var(--chart-navy)"/>
      <rect x="136" y="55" width="16" height="45" fill="var(--chart-navy)"/>
      <g font-size="4.5" fill="#555" text-anchor="middle">
        <text x="58" y="106">A</text><text x="58" y="112">Company</text>
        <text x="101" y="106">B</text><text x="101" y="112">Company</text>
        <text x="144" y="106">C</text><text x="144" y="112">Company</text>
      </g>
    </svg>
  </div>

  <div class="card card-hours">
    <p class="centered" style="margin:2px 0 6px">This results in between six and eight additional hours work per week...</p>
    <div class="hours-row">
      <div>
        <h4>Physicians</h4>
        <svg width="128" height="82" viewBox="0 0 128 82" aria-label="Additional hours per week, physicians">
          <g font-size="4" fill="#555" text-anchor="end">
            <text x="20" y="62">0</text><text x="20" y="47">2</text><text x="20" y="32">4</text><text x="20" y="17">6</text><text x="20" y="5">8</text>
          </g>
          <text x="6" y="38" font-size="5" fill="#555">%</text>
          <line x1="22" y1="60" x2="122" y2="60" stroke="var(--axis)" stroke-width=".5"/>
          <rect x="34" y="30" width="12" height="30" fill="var(--chart-sky)"/>
          <rect x="66" y="22" width="12" height="38" fill="var(--chart-sky)"/>
          <rect x="98" y="37" width="12" height="23" fill="var(--chart-sky)"/>
          <g font-size="4.5" fill="#555" text-anchor="middle"><text x="40" y="66">A</text><text x="72" y="66">B</text><text x="104" y="66">C</text><text x="72" y="74">Company</text></g>
        </svg>
      </div>
      <div>
        <h4>Med Info</h4>
        <svg width="128" height="82" viewBox="0 0 128 82" aria-label="Additional hours per week, medical information">
          <g font-size="4" fill="#555" text-anchor="end">
            <text x="20" y="62">0</text><text x="20" y="45">4</text><text x="20" y="28">8</text><text x="20" y="11">12</text>
          </g>
          <text x="6" y="38" font-size="5" fill="#555">%</text>
          <line x1="22" y1="60" x2="122" y2="60" stroke="var(--axis)" stroke-width=".5"/>
          <rect x="66" y="14" width="12" height="46" fill="var(--chart-purple)"/>
          <rect x="98" y="4" width="12" height="56" fill="var(--chart-purple)"/>
          <g font-size="4.5" fill="#555" text-anchor="middle"><text x="40" y="66">A</text><text x="72" y="66">B</text><text x="104" y="66">C</text><text x="72" y="74">Company</text></g>
        </svg>
      </div>
      <div>
        <h4>SA/MSL*</h4>
        <svg width="128" height="82" viewBox="0 0 128 82" aria-label="Additional hours per week, scientific advisors and medical science liaisons">
          <g font-size="4" fill="#555" text-anchor="end">
            <text x="20" y="62">0</text><text x="20" y="46">5</text><text x="20" y="29">10</text><text x="20" y="13">15</text>
          </g>
          <text x="6" y="38" font-size="5" fill="#555">%</text>
          <line x1="22" y1="60" x2="122" y2="60" stroke="var(--axis)" stroke-width=".5"/>
          <rect x="34" y="31" width="12" height="29" fill="var(--chart-teal)"/>
          <rect x="66" y="34" width="12" height="26" fill="var(--chart-teal)"/>
          <g font-size="4.5" fill="#555" text-anchor="middle"><text x="40" y="66">A</text><text x="72" y="66">B</text><text x="104" y="66">C</text></g>
          <text x="24" y="74" font-size="4" fill="#555">*scientific advisor/medical science liaison</text>
        </svg>
      </div>
    </div>
  </div>

  <div class="card card-friction">
    <h3>% Experience raised levels of friction</h3>
    <p>... and raised levels of friction, reported as ‘frequent’ or ‘common’ by 80% in one organization and to a significant level in all three.</p>
    <h4 style="margin-top:6px">Friction reported as common or frequent</h4>
    <svg width="176" height="72" viewBox="0 0 176 72" aria-label="Bar chart: friction reported as common or frequent">
      <g font-size="4.2" fill="#555" text-anchor="end">
        <text x="24" y="62">0</text><text x="24" y="50">20</text><text x="24" y="38">40</text><text x="24" y="26">60</text><text x="24" y="14">80</text><text x="24" y="3">100</text>
      </g>
      <text x="8" y="34" font-size="5" fill="#555">%</text>
      <line x1="27" y1="60" x2="168" y2="60" stroke="var(--axis)" stroke-width=".5"/>
      <rect x="44" y="20" width="16" height="40" fill="var(--chart-navy)"/>
      <rect x="89" y="11" width="16" height="49" fill="var(--chart-navy)"/>
      <rect x="134" y="15" width="16" height="45" fill="var(--chart-navy)"/>
      <g font-size="4.5" fill="#555" text-anchor="middle"><text x="52" y="67">A</text><text x="97" y="67">B</text><text x="142" y="67">C</text></g>
    </svg>
  </div>

  <div class="card card-deadlines">
    <h3>% Experience missed deadlines</h3>
    <p>Missed deadlines were estimated for around one third of projects.</p>
    <h4 style="margin-top:12px">Missed deadlines</h4>
    <svg width="187" height="80" viewBox="0 0 187 80" aria-label="Bar chart: percent missed deadlines">
      <g font-size="4.2" fill="#555" text-anchor="end">
        <text x="24" y="72">0</text><text x="24" y="64">5</text><text x="24" y="57">10</text><text x="24" y="50">15</text><text x="24" y="43">20</text><text x="24" y="36">25</text><text x="24" y="29">30</text><text x="24" y="22">35</text><text x="24" y="15">40</text><text x="24" y="8">45</text><text x="24" y="1.5">50</text>
      </g>
      <text x="8" y="40" font-size="5" fill="#555">%</text>
      <line x1="27" y1="70" x2="178" y2="70" stroke="var(--axis)" stroke-width=".5"/>
      <rect x="46" y="30" width="16" height="40" fill="var(--chart-sky)"/>
      <rect x="94" y="8" width="16" height="62" fill="var(--chart-sky)"/>
      <rect x="142" y="17" width="16" height="53" fill="var(--chart-sky)"/>
      <g font-size="4.5" fill="#555" text-anchor="middle"><text x="54" y="77">A</text><text x="102" y="77">B</text><text x="150" y="77">C</text></g>
    </svg>
  </div>
</section>

<section class="panel conclusions">
  <div class="pill pill-navy">CONCLUSIONS</div>
  <div class="body">
    <p>Between one third and one half of the available resource in medical affairs teams in the UK is taken up reviewing materials. The distribution of this work varies between organisations, depending on allocation of responsibilities. Materials are seen multiple times and a significant proportion of iterations are seen again and again. This causes loss of productivity and internal friction between and within departments. Scientists and physicians engaged in review have positive proposals for process improvement, which are consistent across the organisations involved in this piece of work.</p>
    <p>This small survey identifies potential best practice. The interventions proposed are not proven to reduce waste in the copy review process. However, it seems likely that pharmaceutical companies could save time and money by adopting some simple solutions aimed at ensuring only good quality, scientifically valid material enters the review cycle, and by defining review standards, roles and responsibilities. Physicians and scientists could be released from desk work to undertake customer facing activities or conduct studies. Hard to fill posts and subsequent reliance on contractors could be reduced.</p>
    <p>This activity has crept up on the industry, to the point now that reviewing copy has become an industry within an industry, occupying half of the working lives of hundreds of medical information specialists and pharmaceutical physicians in the UK. This is not mission critical work and is a diversion from the productive and real work of supporting patients and helping customers to understand medicines.</p>
    <p>An industry-wide prospective survey is necessary to identify actual resource utilisation in this activity and benchmark best vs worst practice. Process improvement interventions could be formally assessed to measure the savings that can be made.</p>
  </div>
  <div class="grey-box">
    <p style="margin-bottom:7px">It is likely that three relatively simple actions could save a lot of time:</p>
    <ul>
      <li>Raise awareness and measure resources used in copy review;</li>
      <li>Improve the standards of materials entering the review cycle;</li>
      <li>Define and limit responsibilities.</li>
    </ul>
  </div>
</section>

<div class="signoff">
  <div class="brand-mark"><i></i>ClinoVerse</div>
  <div class="email">mara@clinoverse-demo.co.uk</div>
</div>
</body>
</html>
```